Tova Meadows brand , chocolate packaging design

Tova Meadows

Products List

CANNABIS INFUSED CHOCOLATE BAR
(4 Flavor Chocolate Bar)
Original Milk chocolate Bar
Cookies N Cream Bar
Strawberry Cheesecake Bar
S’mores Bar

Information Front
-1000 MG THC Per package
-100mg THC per serving
-Made with Belgian Chocolate
-Made with Quality California Cannabis Extracts
-Net weight of bar 50grams
-California triangle warning symbol
-Flavor of chocolate bar

Information Back

-10 Servings per package
-100 mg serving size

-Directions
Wait 1-2 hours for full effect before consuming more.
-Very potent , Keep out of reach of children

-Store at 68-77° F
-Will melt in prolonged heat
-California government warning and ad41notice website

Ingredient list

Milk chocolate Bar
MILK CHOCOLATE (SUGAR, COCOA BUTTER , UNSWEETENED CHOCOLATE, SUNFLOWER LECITHIN, VANILLA) , CANNABIS EXTRACT.
ALLERGENS-CONTAINS MILK

Strawberry Cheesecake
WHITE CHOCOLATE (SUGAR, COCOA BUTTER, WHOLE MILK POWDER ,SOY LECITHIN, NATURAL VANILLA FLAVOR) STRAWBERRY POWDER , STRAWBERRY EXTRACT , NATURAL FLAVORS, CANNABIS EXTRACT.

Cookies n cream
WHITE CHOCOLATE (SUGAR, COCOA BUTTER, WHOLE MILK POWDER ,SOY LECITHIN, NATURAL VANILLA FLAVOR) 9
KRUNDELS (SUGAR, WHITE RICE FLOUR, TAPIOCA STARCH, PALM OIL, CANOLA OIL, WHOLE OAT FLOUR, CORN STARCH , COCOA (PROCESSED WITH ALKALI), INVERT SUGAR, SOY LECITHIN, BAKING SODA, SALT, XANTHAM GUM , CHOCOLATE, ARTIFICIAL FLAVOR, CANNABIS EXTRACT

S’mores
MILK CHOCOLATE (SUGAR, COCOA BUTTER, MILK, UNSWEETENED CHOCOLATE ,SUNFLOWER LECITHIN, VANILLA), MARSHMALLOW (SUGAR ,CORN SYRUP , MODIFIED STARCH, GELATIN, SODIUM HEXAMETAPHOSPHATE, ARTIFICIAL FLAVOR , NATURAL FLAVOR , ARTIFICIAL COLO (BLUE 1)), GRAHAM CRACKER (CORN STARCH, BROWN SUGAR , CORN FLOUR, PALM FAT , SOY FLOUR , SOY BRAN, HONEY, MODIFIED TAPIOCA STARCH, AMMONIUM BICARBONATE, BAKING SODA, SALT, CARAMELIZED SUGAR) NATURAL FLAVOR, CANNABIS EXTRACT.

Looking for simple clean modern design , chocolate bar can be like marivel of like the Brisbury one with images on it , and gummy is a mylar bag I really like the Brisbury style , I can provide dieline etc thank you !

Target Market(s)

Young adults

Industry/Entity Type

Cannabis , Delta 8 , CBD

Requirements
Must have
• Chocolate bar is box , dielines Included with images
Nice to have
• Simple clean , elegant and modern design , like the marivel and Brisbury brands , white logo preferred

```html
<!DOCTYPE html>
<html lang="en">
<head>
<meta charset="utf-8">
<title>Tova Meadows – Cannabis Infused Chocolate Bars</title>
<link rel="stylesheet" href="https://fonts.googleapis.com/css2?family=Anton&family=Oswald:wght@400&family=Roboto:wght@400&display=swap">
<style>
  :root {
    --stage: #f3f3f3;
    --ink: #1c1512;
    --choc-dark: #5a2414;
    --choc-mid: #8a3a22;
    --choc-light: #b5603e;

    --orange-bg: #f7a97e;
    --orange-accent: #a15f3f;
    --orange-title: #fbe6c9;

    --green-bg: #cde4ab;
    --green-accent: #80ad5d;
    --green-title: #fdf6d8;

    --pink-bg: #f7cbcd;
    --pink-accent: #d0817f;
    --pink-title: #fbe0de;

    --blue-bg: #a9dee6;
    --blue-accent: #4db4c9;
    --blue-title: #f2fbfc;
  }

  * { box-sizing: border-box; margin: 0; padding: 0; }

  html, body {
    width: 1125px;
    height: 1200px;
    overflow: hidden;
    background: var(--stage);
  }

  .lineup {
    position: absolute;
    top: 330px;
    left: 37px;
    display: flex;
    gap: 30px;
  }

  .bar-box {
    position: relative;
    width: 240px;
    height: 520px;
    background: var(--bg);
    overflow: hidden;
  }

  .bar-box--milk       { --bg: var(--orange-bg); --accent: var(--orange-accent); --title: var(--orange-title); }
  .bar-box--cookies    { --bg: var(--green-bg);  --accent: var(--green-accent);  --title: var(--green-title); }
  .bar-box--strawberry { --bg: var(--pink-bg);   --accent: var(--pink-accent);   --title: var(--pink-title); }
  .bar-box--smores     { --bg: var(--blue-bg);   --accent: var(--blue-accent);   --title: var(--blue-title); }

  .brand {
    position: absolute;
    top: 42px;
    left: 20px;
    max-width: 172px;
    white-space: nowrap;
    font-family: "Oswald", sans-serif;
    font-weight: 400;
    font-size: 23px;
    letter-spacing: 1px;
    text-transform: uppercase;
    color: var(--ink);
    line-height: 1;
  }

  .warning-mark {
    position: absolute;
    top: 20px;
    right: 14px;
    width: 24px;
    height: 22px;
  }

  .chocolate-splash {
    position: absolute;
    top: 150px;
    left: 40px;
    width: 230px;
    height: 280px;
    border-radius: 60% 10% 30% 50%;
    background:
      radial-gradient(ellipse at 40% 30%, var(--choc-light) 0%, transparent 45%),
      radial-gradient(ellipse at 60% 60%, var(--choc-mid) 0%, var(--choc-dark) 80%);
  }

  .flavor-title {
    position: absolute;
    top: 95px;
    left: 22px;
    width: 196px;
    height: 86px;
    background: var(--accent);
    display: flex;
    align-items: center;
    justify-content: center;
    text-align: center;
    z-index: 2;
  }

  .flavor-title::after {
    content: "";
    position: absolute;
    inset: 5px;
    border: 1px solid var(--bg);
    opacity: 0.8;
  }

  .flavor-title h2 {
    font-family: "Anton", sans-serif;
    font-weight: 400;
    font-size: 25px;
    line-height: 1.12;
    color: var(--title);
  }

  .info-panel {
    position: absolute;
    left: 20px;
    bottom: 16px;
    width: 200px;
    height: 170px;
    background: var(--accent);
    color: #fff;
    text-align: center;
    padding: 10px 10px 8px;
    z-index: 2;
  }

  .info-panel::after {
    content: "";
    position: absolute;
    inset: 5px;
    border: 1px solid var(--bg);
    opacity: 0.8;
  }

  .info-panel h3 {
    font-family: "Anton", sans-serif;
    font-weight: 400;
    font-size: 14.5px;
    line-height: 1.15;
    color: var(--title);
    padding-bottom: 6px;
    border-bottom: 1px solid rgba(255,255,255,0.6);
  }

  .dose-row {
    display: flex;
    border-bottom: 1px solid rgba(255,255,255,0.6);
    padding: 5px 0;
  }

  .dose-row p {
    flex: 1;
    font-family: "Roboto", sans-serif;
    font-size: 8.5px;
    line-height: 1.2;
    text-transform: uppercase;
  }

  .dose-row p + p { border-left: 1px solid rgba(255,255,255,0.6); }

  .origin {
    font-family: "Roboto", sans-serif;
    font-size: 8.5px;
    line-height: 1.25;
    padding: 5px 0;
    border-bottom: 1px solid rgba(255,255,255,0.6);
  }

  .net-weight {
    font-family: "Roboto", sans-serif;
    font-size: 8.5px;
    padding-top: 5px;
  }
</style>
</head>
<body>
  <main class="lineup">

    <article class="bar-box bar-box--milk">
      <p class="brand">Tova Meadows</p>
      <svg class="warning-mark" viewBox="0 0 24 22" aria-hidden="true"><polygon points="12,1 23,21 1,21" fill="none" stroke="#1c1512" stroke-width="1.6"/></svg>
      <div class="flavor-title"><h2>Original Milk<br>Chocolate Bar</h2></div>
      <div class="chocolate-splash" role="img" aria-label="Splash of melted milk chocolate"></div>
      <section class="info-panel">
        <h3>CANNABIS INFUSED<br>CHOCOLATE BAR</h3>
        <div class="dose-row"><p>1000 MG THC<br>Per package</p><p>100MG THC<br>Per serving</p></div>
        <p class="origin">Made with Belgian Chocolate<br>Made with Quality California<br>Cannabis Extracts</p>
        <p class="net-weight">Net WT. 50G</p>
      </section>
    </article>

    <article class="bar-box bar-box--cookies">
      <p class="brand">Tova Meadows</p>
      <svg class="warning-mark" viewBox="0 0 24 22" aria-hidden="true"><polygon points="12,1 23,21 1,21" fill="none" stroke="#1c1512" stroke-width="1.6"/></svg>
      <div class="flavor-title"><h2>Cookies N<br>Cream Bar</h2></div>
      <div class="chocolate-splash" role="img" aria-label="Splash of melted chocolate"></div>
      <section class="info-panel">
        <h3>CANNABIS INFUSED<br>CHOCOLATE BAR</h3>
        <div class="dose-row"><p>1000 MG THC<br>Per package</p><p>100MG THC<br>Per serving</p></div>
        <p class="origin">Made with Belgian Chocolate<br>Made with Quality California<br>Cannabis Extracts</p>
        <p class="net-weight">Net WT. 50G</p>
      </section>
    </article>

    <article class="bar-box bar-box--strawberry">
      <p class="brand">Tova Meadows</p>
      <svg class="warning-mark" viewBox="0 0 24 22" aria-hidden="true"><polygon points="12,1 23,21 1,21" fill="none" stroke="#1c1512" stroke-width="1.6"/></svg>
      <div class="flavor-title"><h2>Strawberry<br>Cheesecake Bar</h2></div>
      <div class="chocolate-splash" role="img" aria-label="Splash of melted chocolate"></div>
      <section class="info-panel">
        <h3>CANNABIS INFUSED<br>CHOCOLATE BAR</h3>
        <div class="dose-row"><p>1000 MG THC<br>Per package</p><p>100MG THC<br>Per serving</p></div>
        <p class="origin">Made with Belgian Chocolate<br>Made with Quality California<br>Cannabis Extracts</p>
        <p class="net-weight">Net WT. 50G</p>
      </section>
    </article>

    <article class="bar-box bar-box--smores">
      <p class="brand">Tova Meadows</p>
      <svg class="warning-mark" viewBox="0 0 24 22" aria-hidden="true"><polygon points="12,1 23,21 1,21" fill="none" stroke="#1c1512" stroke-width="1.6"/></svg>
      <div class="flavor-title"><h2>S’mores Bar</h2></div>
      <div class="chocolate-splash" role="img" aria-label="Splash of melted chocolate"></div>
      <section class="info-panel">
        <h3>CANNABIS INFUSED<br>CHOCOLATE BAR</h3>
        <div class="dose-row"><p>1000 MG THC<br>Per package</p><p>100MG THC<br>Per serving</p></div>
        <p class="origin">Made with Belgian Chocolate<br>Made with Quality California<br>Cannabis Extracts</p>
        <p class="net-weight">Net WT. 50G</p>
      </section>
    </article>

  </main>
</body>
</html>
```